WordPress design for BraxtonVell.com

*****
OVERVIEW
*****
BraxtonVell.com needs a fresh, clean, professional design that effectively illustrates its talent in a thoughtful, impressive, and impactful way.
Vell Architecture & Interiors (www.braxtonvell.com) is a well-established, prestigious, well-publicized New England USA architecture firm. Founded in 1996, the privately-held company specializes in high-end residential projects with a focus on classic New England style architecture.
Business contact information is as noted below:
Address:
Vell Architecture & Interiors
87 Orchard Terrace
Needham, MA 02817
Telephone:
617-555-0138
781-555-0274
Email:
info@braxtonvell.com
An excerpt from the current site describes the outfit with this:
"Our architecture and interior design practices are centered around the philosophy that successful living spaces combine a focus on richly articulated detail and an in-depth knowledge of quality construction techniques."
*****
DESIGN RESEARCH
*****
In reviewing design ideas, the following sites were appealing:
Good
- Marcus Thorne Architects (http://mtaarchitects-example.com/) - Simple and clean, but almost too simple.
Better
- Penrose Galt Architecture (http://www.penrosegalt-example.com/) - Direct portfolio access. Simple and clean.
Best
- Brimwell Architects (http://www.brimwellarchitects-example.com/) - Clean, simple, easy to navigate
- QRV Architecture & Interiors (http://www.qrv-architects-example.com/) - Excellent use of high-resolution media, transitions, and navigation.
Here is an example of what is NOT desired:
Tolland Pryce Architects (http://www.tollandpryce-example.com/) - Cluttered, tight landing page. Uncertain navigation.
*****
OTHER DETAILS
*****
The grey in the Vell Architecture & Interiors logo is hex 636363. The font is unknown.
Updates
Project Deadline Extended
Reason: Hello everyone,
Thank you for your continued patience with this project. As it turns out, a critical member of the decision making team on our client's end has been out of the office this week. She will be back next week and is ready to be fully engaged with this. That said, we are extending the contest for at least 5 days. Next week will be much more active.
Thank you for your understanding.
Glasswick Technology Services
Project Deadline Extended
Reason: Hello everyone,
The customer was on vacation and only returned Monday of this week. That said, we need to extend the deadline for 5 days to afford time for review and comment.
Thank you for your patience! The designs submitted thus far are fantastic!
Thanks again,
Project Deadline Extended
Reason: Hello,
With so many designs, the customer is taking longer than anticipated to review them. They are looking at them offline and will process a large batch of comments when ready.
That said, the contest is being extended again.
Thank you for your continued patience.
Project Deadline Extended
Reason: Hello,
Because there are 108 designs to review and comment on, this is taking much longer than anticipated. That said, the contest is being extended another 5 days to ensure the customer has the desired outcome.
Thank you,
Target Market(s)
- Would-be clients
- Landowners
- Construction firms and general contractors
- High-end residential component manufacturers
- Media outlets
- All others interested in high-end residential architecture and interior design
Industry/Entity Type
Architecture
Requirements
Must have
- - Lots of media capabilities, such as embedded video (via ClipStream is fine), project image gallery, sliders for various functions, and social media integrations
- - At least one large slider on the landing page is critical, as well as space for standard lead-in things, such as news/events, opportunities, project highlights, and the likes
- - A high-resolution project showcase - finished projects and works in progress - is critical
- - A place to highlight business partners with the potential for reciprocation
- Form capabilities for things like information requests and general contacts from the public
- - Design must be handed off in a logically-layered (for WordPress) PSD with any and all additional source files provided (e.g. Photoshop, Illustrator, fonts, etc)
Nice to have
- - The WordPress design should be capable of fitting into the very popular FernLayouts Trellis theme.

```html
<!DOCTYPE html>
<html lang="en">
<head>
<meta charset="utf-8">
<title>Vell Architecture &amp; Interiors</title>
<link href="https://fonts.googleapis.com/css2?family=Raleway:wght@300;400;500;700&family=Lora:ital,wght@1,400;1,700&display=swap" rel="stylesheet">
<style>
:root{
  --page:#efefef;
  --card:#ffffff;
  --ink:#222222;
  --muted:#6a6a6a;
  --rule:#cfcfcf;
  --side:#636363;
  --side-line:#6f6f6f;
  --side-text:#ffffff;
  --foot:#e8e8e8;
}
*{box-sizing:border-box;margin:0;padding:0}
html,body{width:1200px;height:1142px;overflow:hidden}
body{background:var(--page);font-family:"Raleway",sans-serif;color:var(--ink);position:relative}

.tiles{position:absolute;left:36px;top:41px;display:grid;
  grid-template-columns:repeat(4,237px);grid-template-rows:repeat(6,158px);gap:8px}
.card{background:var(--card);position:relative}
.photo{display:block}

.brand{grid-column:1;grid-row:1;padding:28px 0 0 34px}
.brand-name{font-size:29px;font-weight:300;color:var(--side);letter-spacing:3px;line-height:1}
.brand-sub{font-size:8.5px;font-weight:300;color:var(--side);letter-spacing:1.6px;margin-top:4px}
.brand-links{position:absolute;right:12px;bottom:10px;font-size:11px;color:#444;word-spacing:2px}
.brand-links span{margin:0 8px;color:#888}

.text-card{padding:28px 32px}
.text-card h2{font-size:19px;font-weight:700;line-height:24px;margin-bottom:14px}
.text-card p{font-size:12.5px;font-weight:300;line-height:19px;color:var(--muted);margin-bottom:12px}
.text-card ul{list-style:none;font-size:12.5px;font-weight:300;line-height:19px;color:var(--muted)}
.text-card li{padding-left:17px;position:relative}
.text-card li::before{content:"";position:absolute;left:5px;top:7px;width:5px;height:5px;border:1px solid var(--muted);border-radius:50%}
.read-more{position:absolute;left:32px;right:32px;top:274px;border-top:1px solid var(--rule);padding-top:9px;font-size:9.5px;font-weight:700;letter-spacing:.3px;color:var(--ink)}

.reno{grid-column:4;grid-row:1/3}
.arch{grid-column:2;grid-row:3/5}
.interior{grid-column:1;grid-row:4/6}

.portfolio{grid-column:3/5;grid-row:4/6;position:relative;background:linear-gradient(160deg,#6e6c66 0%,#3d3b37 45%,#4a3325 80%,#5a3a24 100%);color:#fff}
.portfolio svg.trophy{position:absolute;left:31px;top:204px}
.portfolio h3{position:absolute;left:31px;top:264px;font-size:14px;font-weight:700;white-space:nowrap}
.portfolio .year{position:absolute;left:31px;top:283px;font-family:"Lora",serif;font-style:italic;font-size:10px}
.portfolio .arrow{position:absolute;right:30px;top:286px}

.quote{grid-column:3;grid-row:6;padding:28px 31px}
.quote blockquote{font-family:"Lora",serif;font-style:italic;font-size:12.5px;line-height:19px;color:var(--ink)}
.quote b{font-weight:700}
.quote cite{position:absolute;right:31px;bottom:12px;font-style:normal;font-size:10px;color:var(--muted)}

.sidebar{position:absolute;left:1042px;top:0;width:158px;height:1142px;background:var(--side);color:var(--side-text)}
.social{height:48px;border-bottom:1px solid var(--side-line);display:flex;gap:11px;padding:18px 0 0 29px}
.social i{width:9px;height:9px;border-radius:50%;background:var(--side-text);display:block}
.sidebar nav a{display:flex;align-items:center;min-height:39.5px;border-bottom:1px solid var(--side-line);padding:6px 20px 6px 24px;font-size:10px;font-weight:700;line-height:10px;color:var(--side-text);text-decoration:none;text-transform:uppercase}
.sidebar nav a.tall{min-height:50px}
.copyright{position:absolute;left:24px;bottom:18px;font-size:10px;line-height:15px}

.footer{position:absolute;left:0;top:1071px;width:1042px;height:71px;background:var(--foot);border-top:1px solid #dedede;
  display:flex;justify-content:center;align-items:center;gap:6px;font-size:9.5px;font-weight:500;color:#777;letter-spacing:.2px}
.footer svg{margin-right:2px;vertical-align:middle}
</style>
</head>
<body>

<main class="tiles">
  <div class="card brand">
    <div class="brand-name">VELL</div>
    <div class="brand-sub">ARCHITECTURE &amp; INTERIORS</div>
    <div class="brand-links">HOME<span>|</span>CONTACT</div>
  </div>

  <div class="photo" style="grid-column:2/4;grid-row:1/3;background:linear-gradient(180deg,#b8bec4 0%,#e4e2da 45%,#d8d2c0 80%,#6f7a58 100%)" role="img" aria-label="Curving modern building beside ornate classic facades"></div>

  <article class="card text-card reno">
    <h2>RENOVATIONS<br>AND ADDITIONS</h2>
    <p>At vero eos et accusamus et iusto odio dignissimos ducimus qui blanditiis praesentium voluptatum deleniti atque corrupti quos dolores et quas molestias excepturi sint</p>
    <div class="read-more">READ MORE</div>
  </article>

  <div class="photo" style="grid-column:1;grid-row:2;background:linear-gradient(180deg,#b7bcc2 0%,#d9cdb4 55%,#6d6458 100%)" role="img" aria-label="Stone apartment building on a city street"></div>
  <div class="photo" style="grid-column:1;grid-row:3;background:linear-gradient(180deg,#5a7fb8 0%,#e8eaec 50%,#b9aa90 85%,#3a3a3a 100%)" role="img" aria-label="White modern house with lit entrance path"></div>

  <article class="card text-card arch">
    <h2>ARCHITECTURE</h2>
    <p>At vero eos et accusamus et iusto odioo</p>
    <ul>
      <li>Residential Construction</li>
      <li>Public Housing</li>
      <li>Commercial Building</li>
      <li>Industrial Facility</li>
      <li>Restoration</li>
    </ul>
    <div class="read-more">READ MORE</div>
  </article>

  <div class="photo" style="grid-column:3;grid-row:3;background:linear-gradient(150deg,#dfe2e4 0%,#8f8a82 45%,#b4afa6 70%,#5b5852 100%)" role="img" aria-label="Curved stainless steel building facade"></div>
  <div class="photo" style="grid-column:4;grid-row:3;background:linear-gradient(180deg,#8e9aa6 0%,#6d7b86 45%,#6c8a3e 75%,#7c776f 100%)" role="img" aria-label="Angular zinc-clad museum beside a classic building"></div>

  <article class="card text-card interior">
    <h2>DESIGN INTERIOR</h2>
    <p>At vero eos et accusamus et iusto odio dignissimos ducimus qui blanditiis praesentium voluptatum deleniti atque corrupti quos dolores et quas molestias excepturi sint .</p>
    <p>At vero eos et accusamus et iusto odio dignissimos ducimus</p>
    <div class="read-more">READ MORE</div>
  </article>

  <section class="portfolio" role="img" aria-label="Spiral staircase in a dark modern interior">
    <svg class="trophy" width="38" height="38" viewBox="0 0 38 38" fill="none" stroke="#fff" stroke-width="2">
      <path d="M10 4h18v10a9 9 0 0 1-18 0z"/>
      <path d="M10 7H4c0 7 3 11 8 12M28 7h6c0 7-3 11-8 12"/>
      <path d="M19 23v7M12 35h14l-2-5H14z"/>
      <path d="M19 8l1.5 3 3.2.4-2.3 2.2.6 3.2-3-1.6-3 1.6.6-3.2-2.3-2.2 3.2-.4z" fill="#fff" stroke="none"/>
    </svg>
    <h3>INTERIOR DESIGN PORTFOLIO</h3>
    <div class="year">2015</div>
    <svg class="arrow" width="18" height="8" viewBox="0 0 18 8" fill="none" stroke="#fff" stroke-width="1.2"><path d="M0 4h17M13 1l4 3-4 3"/></svg>
  </section>

  <div class="photo" style="grid-column:2;grid-row:5;background:linear-gradient(180deg,#d8dde0 0%,#eef0f0 50%,#c7c7c5 80%,#6b6258 100%)" role="img" aria-label="Bright white kitchen island with stools"></div>

  <div class="photo" style="grid-column:1;grid-row:6;background:linear-gradient(180deg,#e6ddd0 0%,#b89a80 40%,#5a4336 75%,#3c3430 100%)" role="img" aria-label="Warm kitchen with dining table"></div>
  <div class="photo" style="grid-column:2;grid-row:6;background:linear-gradient(160deg,#9a9a96 0%,#d5d7d1 40%,#6f8a55 70%,#4a3a2e 100%)" role="img" aria-label="Concrete terrace with dining set and plants"></div>

  <figure class="card quote">
    <blockquote>At vero eos et accusamus <b>dignissimos ducimus</b>, praesentium voluptatum deleniti atque corrupti quos dolores.</blockquote>
    <cite>— John Doe, Founder</cite>
  </figure>

  <div class="photo" style="grid-column:4;grid-row:6;background:linear-gradient(180deg,#e9e3d8 0%,#d6cbb8 50%,#f0ece4 75%,#9c8a74 100%)" role="img" aria-label="Bright living room with cream sofas"></div>
</main>

<aside class="sidebar">
  <div class="social"><i></i><i></i><i></i><i></i></div>
  <nav>
    <a>About</a>
    <a>Architecture</a>
    <a>Interior Design</a>
    <a>Works in Progress</a>
    <a class="tall">Renovations and<br>Additions</a>
    <a class="tall">Publications and<br>Awards</a>
    <a>Affiliates</a>
  </nav>
  <div class="copyright">© 2015,<br>BraxtonVell.com</div>
</aside>

<footer class="footer">
  <svg width="7" height="9" viewBox="0 0 7 9" fill="#777"><path d="M3.5 0A3.5 3.5 0 0 0 0 3.5C0 6 3.5 9 3.5 9S7 6 7 3.5A3.5 3.5 0 0 0 3.5 0zm0 5a1.5 1.5 0 1 1 0-3 1.5 1.5 0 0 1 0 3z"/></svg>
  <span>87 ORCHARD TERRACE NEEDHAM, MA 02817</span>
  <svg width="9" height="9" viewBox="0 0 9 9" fill="#777"><path d="M2 0l1.5 2.3-1 1.2a5 5 0 0 0 3 3l1.2-1L9 7 7.7 9C3.6 8.8.2 5.4 0 1.3z"/></svg>
  <span>617.555.0138</span>
  <svg width="10" height="8" viewBox="0 0 10 8" fill="#777"><path d="M0 0h10v1.2L5 4.5 0 1.2zM0 2.4l5 3.3 5-3.3V8H0z"/></svg>
  <span>INFO@BRAXTONVELL.COM</span>
</footer>

</body>
</html>
```